Silicone cotton stick need a packaging design and logo and product images

Make a visual identity for the brand, a logo and packaging for the product silicone cotton swab and product images to sell on Brimlow Bazaar with 6 images. packaging a maximum of 4 colors should capture attention, and inspire safety and environmental preservation. product images size min 3000 x 3000. Example: https: //plumtrellis.example/collections/eco-friendly-ear-swab/products/plumtrellis-grey-fox-swab

Target Market(s)

Women

Industry/Entity Type

Beauty

Logo Text

quelmora

Font styles to use
Sans Serif

Colors

Designer to choose colors to be used in the design.

Requirements
Must have
• A logo with on color, a packaging design with the template provided. The logo is written on the plastic box in on color it takes, 6 images product to sell on marketplace brimlow, see an example on brimlow with the following link https://www.brimlow.example/Reutilisable-R%C3%A9sistant- R% C3% A9utilisable-Remover-Eco / dp / Q4MTR8WN2J / ref = sr_1_7 __ mk_fr_FR =% C3% 85M% C3% 85% C5% BD% C3% 95% C3% 91% 26amp;? crid = 7KDPLQXR21HJT% 26amp; keywords = + stem + cotton reusable% 26amp; qid = 1684302917% 26amp; sprefix =% cotton + 26amp 2Caps% 2C214%; sr = 8-7
Should not have
• Not copying others, something original and effective, capture attention impotent

```html
<!DOCTYPE html>
<html lang="en">
<head>
<meta charset="utf-8">
<title>Quelmora – Silicone Cotton Swab Packaging</title>
<link rel="stylesheet" href="https://fonts.googleapis.com/css2?family=Playfair+Display:wght@700&family=Open+Sans:wght@700&display=swap">
<style>
  :root {
    --bg-light: #b4b4b4;
    --bg-dark: #4a4a4a;
    --box-black: #1b1b1b;
    --panel-white: #ffffff;
    --leaf-green: #8dc21f;
    --ink: #1b1b1b;
    --white: #ffffff;
  }
  * { margin: 0; padding: 0; box-sizing: border-box; }
  html, body { width: 1200px; height: 1200px; overflow: hidden; }
  body {
    background: linear-gradient(180deg, var(--bg-dark) 0%, #8a8a8a 45%, var(--bg-light) 100%);
    position: relative;
    font-family: "Open Sans", sans-serif;
  }
  .brand-logo {
    position: absolute;
    display: flex;
    align-items: center;
    gap: 14px;
    font-family: "Playfair Display", serif;
    font-weight: 700;
    color: var(--white);
  }
  .brand-logo .mark {
    border-radius: 50%;
    background: var(--leaf-green);
    flex: none;
  }
  .hero-logo { top: 110px; left: 700px; font-size: 72px; letter-spacing: 2px; }
  .hero-logo .mark { width: 34px; height: 34px; }

  .package-net {
    position: absolute;
    top: 230px;
    left: 300px;
    height: 860px;
    display: flex;
  }
  .side-panel {
    width: 150px;
    height: 100%;
    background: var(--box-black);
    position: relative;
    border-right: 1px solid #333;
  }
  .side-icons {
    position: absolute;
    top: 190px;
    left: 0;
    width: 100%;
    display: flex;
    flex-direction: column;
    align-items: center;
    gap: 28px;
  }
  .side-brand {
    position: absolute;
    left: 50%;
    bottom: 170px;
    transform: translateX(-50%) rotate(90deg);
    transform-origin: center;
    font-size: 40px;
    white-space: nowrap;
  }
  .side-brand .mark { width: 18px; height: 18px; }

  .front-panel {
    width: 380px;
    height: 100%;
    background: var(--panel-white);
    position: relative;
    overflow: hidden;
  }
  .front-header {
    height: 170px;
    background: var(--box-black);
    display: flex;
    align-items: center;
    justify-content: center;
  }
  .front-header .brand-logo { position: static; font-size: 42px; }
  .front-header .mark { width: 20px; height: 20px; }
  .product-title {
    margin: 40px 0 0 34px;
    color: var(--leaf-green);
    font-size: 30px;
    line-height: 1.15;
  }
  .front-icons {
    display: flex;
    gap: 24px;
    margin: 26px 0 0 34px;
  }
  .plant-artwork {
    position: absolute;
    left: 0;
    right: 0;
    bottom: 0;
    height: 470px;
    background: linear-gradient(160deg, var(--panel-white) 0%, var(--panel-white) 28%, var(--leaf-green) 52%, var(--box-black) 78%);
  }
</style>
</head>
<body>
  <div class="brand-logo hero-logo"><span class="mark"></span>Quelmora</div>

  <div class="package-net">
    <section class="side-panel">
      <div class="side-icons">
        <svg width="58" height="58" viewBox="0 0 58 58" aria-label="Recyclable">
          <circle cx="29" cy="29" r="26" fill="none" stroke="#fff" stroke-width="3"/>
          <path d="M19 33 A11 11 0 0 1 33 18 M39 25 A11 11 0 0 1 25 40" fill="none" stroke="#fff" stroke-width="3"/>
          <path d="M30 13 L35 18 L29 22 Z M28 45 L23 40 L29 36 Z" fill="#fff"/>
        </svg>
        <svg width="58" height="58" viewBox="0 0 58 58" aria-label="Plant based">
          <circle cx="29" cy="29" r="26" fill="none" stroke="#fff" stroke-width="3"/>
          <path d="M29 42 C28 30 34 20 44 17 C44 30 38 38 29 42 Z M29 42 C26 34 21 30 14 29 C15 37 21 41 29 42 Z" fill="#fff"/>
        </svg>
        <svg width="58" height="58" viewBox="0 0 58 58" aria-label="Certificate badge">
          <circle cx="29" cy="29" r="26" fill="none" stroke="#fff" stroke-width="3"/>
        </svg>
      </div>
      <div class="brand-logo side-brand"><span class="mark"></span>Quelmora</div>
    </section>

    <section class="front-panel">
      <header class="front-header">
        <div class="brand-logo"><span class="mark"></span>Quelmora</div>
      </header>
      <h1 class="product-title">Silicone Cotton<br>Swab</h1>
      <div class="front-icons">
        <svg width="58" height="58" viewBox="0 0 58 58" aria-label="Recyclable">
          <circle cx="29" cy="29" r="26" fill="none" stroke="#1b1b1b" stroke-width="3"/>
          <path d="M19 33 A11 11 0 0 1 33 18 M39 25 A11 11 0 0 1 25 40" fill="none" stroke="#1b1b1b" stroke-width="3"/>
          <path d="M30 13 L35 18 L29 22 Z M28 45 L23 40 L29 36 Z" fill="#1b1b1b"/>
        </svg>
        <svg width="58" height="58" viewBox="0 0 58 58" aria-label="Plant based">
          <circle cx="29" cy="29" r="26" fill="none" stroke="#1b1b1b" stroke-width="3"/>
          <path d="M29 42 C28 30 34 20 44 17 C44 30 38 38 29 42 Z M29 42 C26 34 21 30 14 29 C15 37 21 41 29 42 Z" fill="#1b1b1b"/>
        </svg>
        <svg width="58" height="58" viewBox="0 0 58 58" aria-label="Certificate badge">
          <circle cx="29" cy="29" r="26" fill="none" stroke="#1b1b1b" stroke-width="3"/>
        </svg>
      </div>
      <div class="plant-artwork" role="img" aria-label="Illustration of a green leafy plant stem rising over a black curved hill, with two silicone swabs drawn in the lower left"></div>
    </section>
  </div>
</body>
</html>
```